plovu business card design

plovu is an incubator within RTM Media focused on unlocking the potential in underserved niche micro-verticals on the web. our mission is to rapidly develop and foster emerging micro-verticals bc they are ripe for growth - building interesting and trusted content experiences with unqiue, useful and cutting-edge delivery methods.please do all copy (except for RTM Media, which must look as typed here and in logo) in all lowercase. Also please use spaces between phone # extensions not dashes or periods. I have attached all variations of the logo.
Industry/Entity Type
Business
Contact Information for Business Card
daria feltow, ceo www.plovu.io 218 holbrook lane 3rd floor oakland ca 94731 415 602 0002m 510 985 7966d daria.feltow@plovu.io
Look and feel
Each slider illustrates characteristics of the customer's brand and the style your logo design should communicate.

```html
<!DOCTYPE html>
<html lang="en">
<head>
<meta charset="utf-8">
<title>plovu business card</title>
<link rel="stylesheet" href="https://fonts.googleapis.com/css2?family=Montserrat:wght@400;500&display=swap">
<style>
  :root {
    --backdrop: #8a8c8c;
    --paper: #dcdde0;
    --ink: #231f20;
    --teal: #00807f;
    --teal-soft: #0a8f8d;
    --light-text: #e6e6e6;
    --font-text: "Montserrat", sans-serif;
  }
  * { margin: 0; padding: 0; box-sizing: border-box; }
  html, body {
    width: 1200px; height: 900px; overflow: hidden;
    background: var(--backdrop);
    font-family: var(--font-text);
  }
  .stage {
    position: absolute; left: 0; top: 0;
    width: 1280px; height: 960px;
    transform: scale(0.9375); transform-origin: 0 0;
  }
  .card {
    position: absolute; left: 342px;
    width: 541px; height: 309px; overflow: hidden;
  }
  .card--front { top: 127px; background: var(--paper); }
  .card--back { top: 502px; background: var(--ink); }
  .card__art { position: absolute; inset: 0; width: 100%; height: 100%; }

  .wordmark {
    position: absolute; left: 0; right: 0; text-align: center;
    font-weight: 500; letter-spacing: 1px; line-height: 1;
  }
  .wordmark__name { display: inline-flex; align-items: center; gap: 10px; }
  .wordmark__dot { width: 14px; height: 14px; border-radius: 50%; background: var(--teal); display: inline-block; }
  .card--front .wordmark { top: 36px; color: var(--ink); font-size: 78px; }
  .card--front .tagline { position: absolute; top: 117px; left: 0; right: 0; text-align: center; font-size: 14.5px; color: var(--ink); }

  .card--back .wordmark { top: 142px; color: #fff; font-size: 54px; left: -66px; }
  .card--back .tagline { position: absolute; top: 193px; left: 168px; font-size: 10px; color: #fff; }

  .person {
    position: absolute; right: 279px; top: 203px; text-align: right;
    color: var(--light-text); font-size: 14.5px; line-height: 20px;
  }
  .person__name { color: var(--teal-soft); font-size: 20px; font-weight: 500; line-height: 24px; }
  .person__role { font-size: 16px; line-height: 20px; }
  .divider { position: absolute; left: 279px; top: 206px; width: 1px; height: 78px; background: var(--light-text); }
  .contacts { position: absolute; left: 297px; top: 203px; list-style: none; }
  .contacts li {
    display: flex; align-items: center; gap: 8px;
    height: 20.7px; font-size: 14.5px; color: var(--light-text);
  }
  .contacts svg { width: 13px; height: 13px; fill: var(--teal-soft); flex: none; }
</style>
</head>
<body>
<div class="stage">

  <section class="card card--front">
    <svg class="card__art" viewBox="0 0 541 309" aria-hidden="true">
      <path d="M0,118 C120,152 320,176 541,175 L541,181 C320,183 120,168 0,131 Z" fill="var(--teal)"/>
      <path d="M0,131 C120,168 320,183 541,181 L541,309 L0,309 Z" fill="var(--ink)"/>
    </svg>
    <div class="wordmark"><span class="wordmark__name">plovu<span class="wordmark__dot"></span></span></div>
    <div class="tagline">an RTM Media incubator</div>

    <div class="person">
      <div class="person__name">Daria Feltow</div>
      <div class="person__role">CEO</div>
      <div>218 holbrook lane 3rd floor</div>
      <div>oakland ca 94731</div>
    </div>
    <div class="divider"></div>
    <ul class="contacts">
      <li><svg viewBox="0 0 16 16"><path d="M3.5 1l2.5 3-1.5 2c1 2 3 4 5 5l2-1.5 3 2.5-1.5 2.5C7 15 1 9 1 2.5z"/></svg>415 738 4196</li>
      <li><svg viewBox="0 0 16 16"><path d="M4 0h8v16H4zM5.5 2v10h5V2z"/></svg>510 247 3859</li>
      <li><svg viewBox="0 0 16 16"><path d="M1 3h14v1L8 9 1 4zM1 6l7 5 7-5v7H1z"/></svg>daria.feltow@plovu.io</li>
      <li><svg viewBox="0 0 16 16"><circle cx="8" cy="8" r="7"/><path d="M4 5c2 0 2 2 4 2s1 3 3 3" stroke="#231f20" stroke-width="1.2" fill="none"/></svg>www.plovu.io</li>
    </ul>
  </section>

  <section class="card card--back">
    <svg class="card__art" viewBox="0 0 541 309" role="img" aria-label="Teal ink splash backdrop behind the name">
      <defs>
        <radialGradient id="splash" cx="0.5" cy="0.5" r="0.5">
          <stop offset="0" stop-color="var(--teal)"/>
          <stop offset="0.7" stop-color="var(--teal)"/>
          <stop offset="1" stop-color="var(--teal)" stop-opacity="0"/>
        </radialGradient>
      </defs>
      <ellipse cx="240" cy="185" rx="170" ry="135" fill="url(#splash)"/>
    </svg>
    <div class="wordmark">plovu</div>
    <div class="tagline">an RTM Media incubator</div>
  </section>

</div>
</body>
</html>
```